Store Fixtures Company Card Design

We are looking for a business card design for a store fixture company. "Bright Bargain Shelving Supply" we help small businesses with their start up by providing fixtures required to display their products.
It should have a simple yet innovative design in the front, and a couple of sketch design for some sample products we carry in the back, to give a refined look to our company.
We would like our logo, do have one of our products "display cases" integrated in the design. And the rest of it just a clean look, which gives our address, store hours, and contact number, etc.
The color scheme as seen in the samples can be changed as long as the goal is achieved. The design attached just doesn't give off the direction we are looking to go.
Any off the attached products can be used as sketches in the back design. We do not want any name in the front.

```html
<!DOCTYPE html>
<html lang="en">
<head>
<meta charset="utf-8">
<title>Bright Bargain Shelving Supply – Business Card Options</title>
<link href="https://fonts.googleapis.com/css2?family=Roboto+Condensed:wght@300;400;700&display=swap" rel="stylesheet">
<style>
  :root {
    --teal: #0e8a92;
    --teal-dark: #0b6f78;
    --teal-light: #5cc5c9;
    --orange: #f5a93b;
    --ink: #55575a;
    --ink-dark: #333;
    --line: #2a2a2a;
    --paper: #ffffff;
  }
  * { box-sizing: border-box; margin: 0; padding: 0; }
  html, body { width: 1200px; height: 1137px; overflow: hidden; background: var(--paper); }
  body { position: relative; font-family: "Roboto Condensed", "Arial Narrow", sans-serif; color: var(--ink-dark); }

  .card { position: absolute; width: 552px; height: 314px; border: 1px solid var(--line); background: var(--paper); overflow: hidden; }
  .card--back { width: 554px; }

  .option-label { position: absolute; width: 136px; height: 46px; border: 1px solid var(--line); border-top: none;
    display: flex; align-items: center; justify-content: center; font-family: Arial, Helvetica, sans-serif; font-size: 22px; color: #111; }

  /* front */
  .product-photo { position: absolute; left: 0; top: 0; width: 192px; height: 314px;
    background: linear-gradient(180deg, #f4f6f6 0%, #e7ecec 70%, #cfd6d6 92%, #5a5a5c 100%); }
  .logo { position: absolute; display: flex; align-items: center; gap: 8px; }
  .logo__dot { border-radius: 50%; background: var(--teal-dark); flex: none; }
  .logo__name { font-weight: 700; color: var(--teal-light); letter-spacing: 1px; }

  .company-name { position: absolute; right: 31px; top: 24px; text-align: right; line-height: 1; }
  .company-name__top { font-size: 33px; color: var(--ink); font-weight: 400; }
  .company-name__top b { color: var(--teal); font-weight: 700; }
  .company-name__bottom { font-size: 27px; font-weight: 300; color: var(--ink); letter-spacing: 1.5px; margin-top: 4px; }

  .rule { position: absolute; left: 197px; width: 321px; }
  .rule--solid { top: 102px; border-top: 2px solid var(--teal); }
  .rule--dashed { top: 109px; border-top: 2px dashed var(--teal-light); }

  .address { position: absolute; right: 36px; top: 136px; text-align: right; }
  .address__street { font-size: 16px; font-weight: 700; color: var(--ink-dark); line-height: 19px; }
  .address__line { font-size: 11.5px; color: var(--ink); line-height: 14px; }

  .divider { position: absolute; left: 330px; width: 187px; top: 217px; border-top: 1px solid var(--ink); }
  .hours { position: absolute; right: 36px; top: 229px; text-align: right; font-size: 14px; line-height: 17px; color: var(--ink-dark); }
  .hours b { font-weight: 700; }

  /* back */
  .person { position: absolute; left: 25px; top: 134px; }
  .person__name { font-size: 15px; font-weight: 700; color: var(--ink-dark); text-transform: uppercase; letter-spacing: .3px; }
  .person__role { font-size: 10.5px; color: var(--ink); text-transform: uppercase; }
  .person--mixed .person__name { text-transform: none; }

  .product-sketch { position: absolute; left: 205px; top: 42px; width: 336px; height: 246px;
    background: linear-gradient(160deg, #f6f6f6 0%, #c9c9c9 45%, #8e8e8e 100%); border: 1px solid #999; }
  .accent-pattern { position: absolute; left: 379px; top: 0; width: 175px; height: 216px;
    background: linear-gradient(200deg, rgba(92,197,201,.55) 0%, rgba(92,197,201,.15) 60%, rgba(92,197,201,0) 100%); }
</style>
</head>
<body>

<!-- Option A -->
<section class="card card--front" style="left:58px; top:6px;">
  <div class="product-photo" role="img" aria-label="Photo of a glass corner display case"></div>
  <div class="logo" style="left:34px; top:14px;">
    <span class="logo__dot" style="width:70px; height:70px;"></span>
    <span class="logo__name" style="font-size:36px;">BBSS</span>
  </div>
  <h1 class="company-name">
    <div class="company-name__top">BRIGHT <b>BARGAIN</b></div>
    <div class="company-name__bottom">SHELVING SUPPLY</div>
  </h1>
  <div class="rule rule--solid"></div>
  <div class="rule rule--dashed"></div>
  <address class="address" style="font-style:normal;">
    <div class="address__street">4580 Larkfield Avenue</div>
    <div class="address__line">Austin, TX 78745</div>
    <div class="address__line">Tel: 512.555.0142</div>
    <div class="address__line">Fax: 512.555.0187</div>
  </address>
  <div class="divider"></div>
  <div class="hours"><div><b>Mon - Fri:</b> 9:30 am-6pm</div><div><b>Sat :</b>10am -4pm</div></div>
</section>
<div class="option-label" style="left:474px; top:320px;">A</div>

<section class="card card--back" style="left:629px; top:6px;">
  <div class="person"><div class="person__name">Daniel Whitford</div><div class="person__role">Manager</div></div>
  <div class="product-sketch" role="img" aria-label="Pencil sketch of a glass showcase counter"></div>
  <div class="accent-pattern" role="img" aria-label="Faint teal hexagon decoration"></div>
</section>

<!-- Option B -->
<section class="card card--front" style="left:58px; top:385px;">
  <div class="product-photo" role="img" aria-label="Photo of a glass corner display case"></div>
  <div class="logo" style="left:150px; top:30px;">
    <span class="logo__dot" style="width:48px; height:48px; background:var(--orange);"></span>
    <span class="logo__name" style="font-size:22px;">BBSS</span>
  </div>
  <h1 class="company-name">
    <div class="company-name__top">BRIGHT <b>BARGAIN</b></div>
    <div class="company-name__bottom">SHELVING SUPPLY</div>
  </h1>
  <div class="rule rule--solid"></div>
  <div class="rule rule--dashed"></div>
  <address class="address" style="font-style:normal;">
    <div class="address__street">4580 Larkfield Avenue</div>
    <div class="address__line">Austin, TX 78745</div>
    <div class="address__line">Tel: 512.555.0142</div>
    <div class="address__line">Fax: 512.555.0187</div>
  </address>
  <div class="divider" style="border-color:var(--teal);"></div>
  <div class="hours"><div><b>Mon - Fri:</b> 9:30 am-6pm</div><div><b>Sat :</b>10am -4pm</div></div>
</section>
<div class="option-label" style="left:474px; top:700px;">B</div>

<section class="card card--back" style="left:629px; top:388px;">
  <div class="person"><div class="person__name">Samuel Whitford</div><div class="person__role">Operations Manager</div></div>
  <div class="product-sketch" role="img" aria-label="Pencil sketch of a glass showcase counter"></div>
  <div class="accent-pattern" role="img" aria-label="Faint teal hexagon decoration"></div>
</section>

<!-- Option C -->
<section class="card card--front" style="left:60px; top:768px;">
  <div class="product-photo" role="img" aria-label="Photo of a glass corner display case"></div>
  <div class="logo" style="left:34px; top:14px;">
    <span class="logo__dot" style="width:70px; height:70px;"></span>
    <span class="logo__name" style="font-size:36px; color:var(--orange);">BBSS</span>
  </div>
  <h1 class="company-name">
    <div class="company-name__top">BRIGHT <b>BARGAIN</b></div>
    <div class="company-name__bottom">SHELVING SUPPLY</div>
  </h1>
  <div class="rule rule--solid"></div>
  <div class="rule rule--dashed"></div>
  <address class="address" style="font-style:normal;">
    <div class="address__street">4580 Larkfield Avenue</div>
    <div class="address__line">Austin, TX 78745</div>
    <div class="address__line">Tel: 512.555.0142</div>
    <div class="address__line">Fax: 512.555.0187</div>
  </address>
  <div class="divider"></div>
  <div class="hours"><div><b>Mon - Fri:</b> 9:30 am-6pm</div><div><b>Sat :</b>10am -4pm</div></div>
</section>
<div class="option-label" style="left:476px; top:1082px;">C</div>

<section class="card card--back" style="left:629px; top:768px;">
  <div class="person person--mixed"><div class="person__name">Laura Medina</div><div class="person__role">Sales Manager</div></div>
  <div class="product-sketch" role="img" aria-label="Pencil sketch of a glass showcase counter"></div>
  <div class="accent-pattern" role="img" aria-label="Faint teal hexagon decoration"></div>
</section>

</body>
</html>
```